BLOGPRESS Design for a Business Blog

We are running the finance blog kivo.net and want to renew our web page design. Thus, we need a new designed BLOGPRESS theme containing an overview page, used on the front page and the start pages of the categories, and a single article view like on http://kivo.net/blog/coping-with-falling-dollar/ . The new look should be serious, should contain all elements of the current website, should look professional (no entertainment elements) and in light colors.
Updates

Reason: Due to some request, we've extended the deadline a few days.

Reason: Hello,

we received a comment that our budget is to low for  a complete BLOGPRESS design including coding. Thus, we changed our requriement to psd design  only,  without coding.

Industry/Entity Type

Entertainment

Requirements
Must have
• * Light colors
* Two column layout
* Contain all elements of the current website www.kivo.net
Should not have
• * Too much colors
* Look to flashy

```html
<!DOCTYPE html>
<html lang="en">
<head>
<meta charset="utf-8">
<title>kivo.net — finance blog</title>
<link href="https://fonts.googleapis.com/css2?family=Arimo:wght@400;700&family=Tinos&display=swap" rel="stylesheet">
<style>
:root{
  --page:#ffffff;
  --shell:#f6f7f6;
  --topbar:#9fcd7f;
  --topbar-active:#bfe0a5;
  --teal:#17706c;
  --teal-dark:#0f5553;
  --green:#2f8a3e;
  --green-soft:#9fcf86;
  --logo:#8dbf6b;
  --heading:#17706c;
  --text:#555;
  --muted:#8a8a8a;
  --line:#d9dcd9;
  --box:#ffffff;
}
*{box-sizing:border-box;margin:0;padding:0}
html,body{width:1160px;height:1200px;overflow:hidden;background:var(--page)}
body{font-family:"Arimo",Arial,sans-serif;color:var(--text);font-size:8px}
.canvas{position:relative;width:1160px;height:1200px;overflow:hidden}
.shell{position:absolute;left:180px;top:0;width:789px;height:1200px;background:var(--shell)}
.abs{position:absolute}

/* top utility bar */
.topbar{position:absolute;left:180px;top:0;width:789px;height:16px;background:var(--topbar)}
.topbar a{position:absolute;top:0;height:16px;line-height:15px;font-size:6.5px;color:#3b5e2e;text-decoration:none;padding:0 7px}
.topbar a.active{background:var(--topbar-active);color:#2d5a23}
.social{position:absolute;top:3px;width:10px;height:10px;border-radius:2px}

/* brand */
.brand{position:absolute;left:0;top:33px;width:1160px;text-align:center;font-weight:700;font-size:28px;letter-spacing:2px;color:var(--logo)}
.tagline{position:absolute;left:0;top:67px;width:1160px;text-align:center;font-family:"Tinos",serif;font-size:6.5px;color:var(--teal);letter-spacing:.3px}

/* main nav */
.mainnav{position:absolute;left:240px;top:97px;width:669px;height:25px;background:var(--teal);border-radius:4px;border-bottom:2px solid var(--teal-dark)}
.mainnav span{position:absolute;top:0;line-height:24px;font-size:8px;font-weight:700;color:#fff;letter-spacing:.5px}
.mainnav span.current{color:#c9e79e}
.search{position:absolute;left:540px;top:4px;width:123px;height:16px;background:#fff;border-radius:2px;font-size:7px;color:#777;line-height:16px;padding-left:6px}

/* content panel */
.panel{position:absolute;left:241px;top:127px;width:668px;height:1035px;background:#fff;border:1px solid #e6e8e6;border-radius:6px}

.featured{position:absolute;left:256px;top:139px;width:398px;height:164px;background:linear-gradient(160deg,#c8612c 0%,#8b3b2a 35%,#3d3f58 70%,#23283a 100%)}
.flag{position:absolute;left:253px;top:144px;width:105px;height:17px;background:var(--green-soft);font-size:7px;font-weight:700;color:#2c4e22;line-height:17px;padding-left:16px}
.featured-title{position:absolute;left:264px;top:268px;font-size:13px;font-weight:700;color:#fff}
.featured-date{position:absolute;left:269px;top:287px;font-family:"Tinos",serif;font-size:8px;color:#eee}
.dot{position:absolute;top:290px;width:6px;height:6px;border-radius:50%;background:#8dc46a}

.sec-title{position:absolute;font-size:9px;font-weight:700;color:var(--heading)}
.rule{position:absolute;height:0;border-top:1px dotted #999}
.thumb{position:absolute;border:1px solid #ccc;padding:2px;background:#fff}
.thumb i{display:block;width:100%;height:100%}
.mini-title{position:absolute;font-size:10.5px;font-weight:700;color:var(--green);line-height:11.5px;width:118px}
.date{position:absolute;font-family:"Tinos",serif;font-size:7.5px;color:#555}

.entry-title{position:absolute;left:364px;font-size:11px;font-weight:700;color:var(--green)}
.excerpt{position:absolute;left:364px;width:295px;font-size:7px;line-height:10px;color:#555}
.excerpt u{color:var(--green)}
.comments{position:absolute;left:253px;width:46px;height:7px;background:#111;color:#fff;font-size:5px;line-height:7px;padding-left:4px}

/* sidebar */
.box{position:absolute;background:var(--box);border:1px solid #e3e6e3}
.video{position:absolute;left:684px;top:143px;width:203px;height:137px;background:linear-gradient(180deg,#e6e6e6,#b9bbb6 60%,#5c5e5a)}
.video-label{position:absolute;left:684px;top:143px;width:203px;height:20px;background:var(--green-soft);font-size:10px;font-weight:700;color:var(--teal);line-height:20px;padding-left:10px}
.player{position:absolute;left:684px;top:265px;width:203px;height:14px;background:#e0e0e0;border-top:1px solid #bbb}
.sub-row{position:absolute;left:712px;font-size:8px;color:#555}
.pop-head{position:absolute;left:695px;top:370px;font-size:11px;color:var(--teal)}
.pop-title{position:absolute;left:698px;font-size:8px;font-weight:700;color:var(--green)}
.pop-meta{position:absolute;left:698px;font-family:"Tinos",serif;font-size:6.5px;color:#888}
.small-head{position:absolute;font-size:8px;font-weight:700;color:var(--teal)}
.list-item{position:absolute;font-size:7px;color:#444}
.tiny{position:absolute;font-size:7px;line-height:10px;color:#555;width:82px}
.tiny b{color:var(--teal)}
.spons{position:absolute;left:798px;width:80px;font-size:5.5px;line-height:6.5px;color:#555}
.spons u{font-weight:700;color:#333}
.spons em{font-style:normal;color:var(--teal)}
.ad-line{position:absolute;left:690px;top:1093px;font-size:10.5px;color:var(--green);letter-spacing:.3px}

.footer{position:absolute;top:1166px;font-size:7px;color:#555}
.footer.right{color:var(--teal)}
</style>
</head>
<body>
<div class="canvas">
  <div class="shell"></div>

  <nav class="topbar">
    <a class="active" style="left:76px">Home</a>
    <a style="left:118px">About Us</a>
    <a style="left:170px">FAQ</a>
    <a style="left:208px">Support</a>
    <a style="left:255px">Advertise</a>
    <a style="left:310px">Archive Pages</a>
    <a style="left:380px">Contact Us</a>
    <span class="social" style="left:695px;background:#f39b2b"></span>
    <span class="social" style="left:713px;background:#5fb7e5"></span>
  </nav>

  <div class="brand">kivo.net</div>
  <div class="tagline">KIVO.NET IS ALL ABOUT ACHIEVING YOUR FINANCIAL GOALS</div>

  <nav class="mainnav">
    <span class="current" style="left:16px">HOME</span>
    <span style="left:73px">FINANCE</span>
    <span style="left:145px">ECONOMY</span>
    <span style="left:223px">RESOURCES</span>
    <span style="left:312px">PERSONAL SAVING</span>
    <span style="left:432px">MAKE MONEY</span>
    <div class="search">Search here
      <svg width="11" height="11" viewBox="0 0 11 11" style="position:absolute;right:4px;top:3px"><circle cx="4.5" cy="4.5" r="3.3" fill="none" stroke="#555" stroke-width="1.2"/><line x1="7" y1="7" x2="10" y2="10" stroke="#555" stroke-width="1.4"/></svg>
    </div>
  </nav>

  <div class="panel"></div>

  <!-- featured -->
  <div class="featured" role="img" aria-label="Photo of a shopper carrying colourful shopping bags"></div>
  <div class="flag">FEATURED NEWS</div>
  <div class="featured-title">Something Old: Something New?</div>
  <div class="featured-date">- 22 Apr 2011</div>
  <span class="dot" style="left:590px;background:#5c8d45"></span>
  <span class="dot" style="left:603px"></span>
  <span class="dot" style="left:616px"></span>
  <span class="dot" style="left:629px"></span>
  <span class="dot" style="left:642px"></span>

  <!-- category columns -->
  <div class="rule" style="left:255px;top:321px;width:187px"></div>
  <div class="rule" style="left:468px;top:321px;width:187px"></div>
  <div class="sec-title" style="left:255px;top:324px">Personal saving</div>
  <div class="sec-title" style="left:469px;top:324px">Economy</div>
  <div class="rule" style="left:255px;top:337px;width:187px"></div>
  <div class="rule" style="left:468px;top:337px;width:187px"></div>

  <div class="thumb" style="left:256px;top:347px;width:61px;height:40px"><i role="img" aria-label="Cartoon sketch about saving money" style="background:#e9e9e9"></i></div>
  <div class="mini-title" style="left:322px;top:345px">Money/ Saving Jokes</div>
  <div class="date" style="left:324px;top:379px">1 Jun 2011</div>

  <div class="thumb" style="left:467px;top:347px;width:61px;height:40px"><i role="img" aria-label="Coins and a small card" style="background:linear-gradient(#f0f0f0,#c9c4b8)"></i></div>
  <div class="mini-title" style="left:533px;top:345px">6 Secrets to Suc-cessful Saving</div>
  <div class="date" style="left:534px;top:379px">11 Apr 2011</div>

  <div class="rule" style="left:255px;top:403px;width:187px"></div>
  <div class="rule" style="left:468px;top:403px;width:187px"></div>

  <div class="thumb" style="left:256px;top:416px;width:61px;height:40px"><i role="img" aria-label="Euro coin chained to a weight" style="background:linear-gradient(#f4f4f4,#9a9a9a)"></i></div>
  <div class="mini-title" style="left:324px;top:416px">Surviving the Euro Crisis</div>
  <div class="date" style="left:324px;top:451px">20 May 2011</div>

  <div class="thumb" style="left:467px;top:416px;width:61px;height:40px"><i role="img" aria-label="Hands holding the globe" style="background:linear-gradient(#2a62b0,#6aa0d8)"></i></div>
  <div class="mini-title" style="left:533px;top:416px;width:120px">Saving the Environ-ment: Saving Your Money</div>
  <div class="date" style="left:533px;top:452px">10 Apr 2011</div>

  <div class="rule" style="left:255px;top:477px;width:187px"></div>
  <div class="rule" style="left:468px;top:477px;width:187px"></div>

  <div class="thumb" style="left:256px;top:490px;width:61px;height:40px"><i role="img" aria-label="Dollar bill in a shredder" style="background:linear-gradient(#eee,#8e9c83)"></i></div>
  <div class="mini-title" style="left:324px;top:490px">Coping With Falling Dollar</div>
  <div class="date" style="left:323px;top:526px">10 May 2011</div>

  <div class="thumb" style="left:467px;top:490px;width:61px;height:40px"><i role="img" aria-label="Shoppers in a supermarket aisle" style="background:linear-gradient(90deg,#d66c4a,#7aa0c8)"></i></div>
  <div class="mini-title" style="left:533px;top:490px">Product Labels: More Than Meets The Eye</div>
  <div class="date" style="left:533px;top:526px">16 Mar 2011</div>

  <!-- latest entries -->
  <div class="sec-title" style="left:255px;top:567px">Latest Entries</div>
  <div class="rule" style="left:255px;top:580px;width:400px"></div>

  <div class="thumb" style="left:255px;top:592px;width:97px;height:61px"><i role="img" aria-label="Tax form with calculator" style="background:linear-gradient(135deg,#f2f2f2,#a8a8a8)"></i></div>
  <div class="comments" style="top:642px">2 Comments</div>
  <div class="entry-title" style="top:592px">11 Tax Tips: Organize Your Finances in 2011</div>
  <div class="date" style="left:365px;top:615px">28 Feb 2011</div>
  <div class="excerpt" style="top:629px">As another new year starts, each one of us is hoping for and planning to begin a new life, a better and happier one than last year. As a New Year tradition, we have learned to make resolutions like going on a diet, <u>more...</u></div>

  <div class="thumb" style="left:255px;top:680px;width:97px;height:61px"><i role="img" aria-label="No new taxes sign with thumbs down" style="background:#e3141b"></i></div>
  <div class="comments" style="top:730px">8 Comments</div>
  <div class="entry-title" style="top:680px">Weird Taxes? Scary Taxes?</div>
  <div class="date" style="left:365px;top:692px">20 Feb 2011</div>
  <div class="excerpt" style="top:706px">As if we're not already taxed more than enough on almost everything that we do, eat or go, there are even new taxes, weird taxes to be exact, that we may not be aware of but should be starting now <u>more...</u></div>

  <div class="thumb" style="left:255px;top:768px;width:97px;height:61px"><i role="img" aria-label="Graduate mother holding her baby" style="background:linear-gradient(135deg,#3a6a9c,#8fb06b)"></i></div>
  <div class="comments" style="top:818px">4 Comments</div>
  <div class="entry-title" style="top:768px">Educational Aid for Single Moms: Will You Qualify?</div>
  <div class="date" style="left:365px;top:791px">22 Jan 2011</div>
  <div class="excerpt" style="top:805px">If you have been following previous posts from Kivo.net, you will learn of so many options on how single moms can get assistance. But apart from the federal welfare services, <u>more...</u></div>

  <div class="thumb" style="left:255px;top:856px;width:97px;height:61px"><i role="img" aria-label="Tax form with calculator" style="background:linear-gradient(135deg,#f2f2f2,#a8a8a8)"></i></div>
  <div class="comments" style="top:906px">2 Comments</div>
  <div class="entry-title" style="top:856px">Other latest entries titles goes here</div>
  <div class="date" style="left:365px;top:879px">28 Feb 2011</div>
  <div class="excerpt" style="top:893px">As another new year starts, each one of us is hoping for and planning to begin a new life, a better and happier one than last year. As a New Year tradition, we have learned to make resolutions like going on a diet, <u>more...</u></div>

  <div class="thumb" style="left:255px;top:944px;width:97px;height:61px"><i role="img" aria-label="No new taxes sign with thumbs down" style="background:#e3141b"></i></div>
  <div class="comments" style="top:994px">8 Comments</div>
  <div class="entry-title" style="top:944px">Other latest entries titles goes here</div>
  <div class="date" style="left:365px;top:956px">20 Feb 2011</div>
  <div class="excerpt" style="top:970px">As if we're not already taxed more than enough on almost everything that we do, eat or go, there are even new taxes, weird taxes to be exact, that we may not be aware of but should be starting now <u>more...</u></div>

  <div class="thumb" style="left:255px;top:1032px;width:97px;height:61px"><i role="img" aria-label="Graduate mother holding her baby" style="background:linear-gradient(135deg,#3a6a9c,#8fb06b)"></i></div>
  <div class="comments" style="top:1082px">4 Comments</div>
  <div class="entry-title" style="top:1032px">Other latest entries titles goes here</div>
  <div class="date" style="left:365px;top:1055px">22 Jan 2011</div>
  <div class="excerpt" style="top:1069px">If you have been following previous posts from Kivo.net, you will learn of so many options on how single moms can get assistance. But apart from the federal welfare services, <u>more...</u></div>

  <div class="rule" style="left:255px;top:1140px;width:400px"></div>

  <!-- sidebar: video -->
  <div class="video" role="img" aria-label="Video still of dollar bills going down a drain"></div>
  <div class="video-label">Examining the Roots</div>
  <svg class="abs" style="left:762px;top:198px" width="46" height="27" viewBox="0 0 46 27"><rect x="1" y="1" width="44" height="25" rx="5" fill="#eee" fill-opacity=".8" stroke="#999"/><path d="M19 7 L29 13.5 L19 20 Z" fill="#666"/></svg>
  <div class="player">
    <svg width="203" height="13" viewBox="0 0 203 13"><path d="M5 3 L11 6.5 L5 10 Z" fill="#333"/><rect x="20" y="4" width="3" height="5" fill="#333"/><path d="M23 4 L28 2 L28 11 L23 9 Z" fill="#333"/><text x="43" y="9" font-size="6" font-family="Arimo,Arial,sans-serif" fill="#333">0:00 / 2:29</text><rect x="86" y="5" width="86" height="3" rx="1.5" fill="#bbb"/><circle cx="90" cy="6.5" r="3.5" fill="#777"/><rect x="187" y="3" width="8" height="7" fill="none" stroke="#333"/></svg>
  </div>

  <!-- subscribe -->
  <div class="box" style="left:684px;top:289px;width:203px;height:66px"></div>
  <svg class="abs" style="left:695px;top:296px" width="10" height="8" viewBox="0 0 10 8"><rect x=".5" y=".5" width="9" height="7" fill="#fff" stroke="#7aa5c8"/><path d="M.5 .5 L5 4.5 L9.5 .5" fill="none" stroke="#7aa5c8"/></svg>
  <div class="sub-row" style="top:296px">Get updates via email</div>
  <div class="rule" style="left:692px;top:309px;width:188px;border-top:1px solid #eee"></div>
  <svg class="abs" style="left:695px;top:315px" width="9" height="9" viewBox="0 0 9 9"><rect width="9" height="9" rx="1.5" fill="#f39b2b"/><circle cx="2.3" cy="6.7" r="1" fill="#fff"/><path d="M1.5 4 A3.5 3.5 0 0 1 5 7.5 M1.5 1.5 A6 6 0 0 1 7.5 7.5" fill="none" stroke="#fff" stroke-width="1"/></svg>
  <div class="sub-row" style="top:315px">Subscribe via RSS</div>
  <div class="rule" style="left:692px;top:328px;width:188px;border-top:1px solid #eee"></div>
  <span class="abs" style="left:695px;top:334px;width:9px;height:9px;border-radius:2px;background:#5fb7e5"></span>
  <div class="sub-row" style="top:334px">Follow us on Chirper</div>

  <!-- popular posts -->
  <div class="box" style="left:684px;top:364px;width:203px;height:191px"></div>
  <div class="pop-head">Popular Posts</div>
  <div class="rule" style="left:686px;top:389px;width:199px"></div>
  <div class="pop-title" style="top:397px">Teaching Our Kids About Money</div>
  <div class="pop-meta" style="top:408px">Posted on 1 Jun 2011 // 32 comments</div>
  <div class="pop-title" style="top:431px">Smart Online Shopping Tips</div>
  <div class="pop-meta" style="top:442px">Posted on 2 Jun 2011 // 24 comments</div>
  <div class="pop-title" style="top:460px">Work After Retirement:</div>
  <div class="pop-meta" style="top:471px">Posted on 11 Jun 2011 // 15 comments</div>
  <div class="pop-title" style="top:490px">Will You Inherit Your Parents' Debt?</div>
  <div class="pop-meta" style="top:501px">Posted on 12 Jun 2011 // 23 comments</div>
  <div class="pop-title" style="top:522px">Raking More Cash in 2011</div>
  <div class="pop-meta" style="top:533px">Posted on 22 Jun 2011 // 13 comments</div>

  <!-- ad block -->
  <svg class="abs" style="left:698px;top:573px" width="179" height="142" viewBox="0 0 179 142"><rect x=".5" y=".5" width="178" height="141" fill="#f7f8f7" stroke="#e2e5e2"/><line x1="0" y1="0" x2="179" y2="142" stroke="#ccc" stroke-dasharray="3 3"/><line x1="179" y1="0" x2="0" y2="142" stroke="#ccc" stroke-dasharray="3 3"/></svg>
  <div class="abs" style="left:752px;top:622px;font-size:13px;font-weight:700;color:#222;line-height:16px;background:#f7f8f7">Your<br>ADS<br>HERE</div>

  <!-- archives / tags -->
  <div class="box" style="left:685px;top:733px;width:97px;height:108px"></div>
  <div class="small-head" style="left:692px;top:739px">Archives</div>
  <div class="rule" style="left:686px;top:752px;width:95px;border-top:1px solid #e3e3e3"></div>
  <div class="list-item" style="left:693px;top:758px">August 2011</div>
  <div class="list-item" style="left:693px;top:774px">July 2011</div>
  <div class="list-item" style="left:693px;top:790px">June 2011</div>
  <div class="list-item" style="left:693px;top:806px">May 2010</div>
  <div class="list-item" style="left:693px;top:823px">April 2010</div>

  <div class="box" style="left:790px;top:733px;width:97px;height:108px"></div>
  <div class="small-head" style="left:797px;top:739px">Tags</div>
  <div class="rule" style="left:791px;top:752px;width:95px;border-top:1px solid #e3e3e3"></div>
  <div class="list-item" style="left:798px;top:758px">Financial planner</div>
  <div class="list-item" style="left:798px;top:774px">Financial planning</div>
  <div class="list-item" style="left:798px;top:790px">Frugal lifestyle</div>
  <div class="list-item" style="left:798px;top:806px">Overspending</div>
  <div class="list-item" style="left:798px;top:823px">Save money</div>

  <!-- most commented / sponsored -->
  <div class="box" style="left:685px;top:849px;width:97px;height:204px"></div>
  <div class="small-head" style="left:691px;top:854px">Most Commented</div>
  <div class="rule" style="left:686px;top:867px;width:95px;border-top:1px solid #e3e3e3"></div>
  <div class="tiny" style="left:693px;top:871px"><b>Person name :</b> Lorem ipsum dolor sit amet, consectetur adipiscing elit. Duis sit amet dolor arcu.</div>
  <div class="tiny" style="left:693px;top:935px"><b>Ijem ja :</b> Lorem ipsum dolor sit amet, consectetur adipi-scing elit. Duis sit amet dolor arcu.</div>
  <div class="tiny" style="left:693px;top:999px"><b>Tahi :</b> Lorem ipsum dolor sit amet, con-sectetur adipiscing elit. Duis sit amet</div>

  <div class="box" style="left:790px;top:849px;width:97px;height:204px"></div>
  <div class="small-head" style="left:797px;top:854px">Sponsored Links</div>
  <div class="rule" style="left:791px;top:867px;width:95px;border-top:1px solid #e3e3e3"></div>
  <div class="spons" style="top:872px"><u>Sample (ad.sample)</u><br>Lorem ipsum dolor sit amet, consectetur adipiscing elit...<br><em>www.adsample.com</em></div>
  <div class="rule" style="left:796px;top:920px;width:84px;border-top:1px solid #eee"></div>
  <div class="spons" style="top:926px"><u>Sample (ad.sample)</u><br>Lorem ipsum dolor sit amet, consectetur adipiscing elit...<br><em>www.adsample.com</em></div>
  <div class="rule" style="left:796px;top:976px;width:84px;border-top:1px solid #eee"></div>
  <div class="spons" style="top:983px"><u>Sample (ad.sample)</u><br>Lorem ipsum dolor sit amet, consectetur adipiscing elit...<br><em>www.adsample.com</em></div>
  <div class="abs" style="left:827px;top:1040px;font-size:5.5px;color:#333">Ads by <span style="font-size:8px;color:#555">Adnet</span></div>

  <div class="abs" style="left:683px;top:1062px;width:204px;height:80px;background:#f8faf8"></div>
  <div class="ad-line">Your advertisement can placed here</div>

  <!-- footer -->
  <div class="footer" style="left:257px">Copyright © 2010 BLOGPRESS All rights reserved, designed by KIVOdotNET</div>
  <div class="footer right" style="left:755px">Terms &amp; Conditions &nbsp;&nbsp;<span style="color:#777">|</span>&nbsp;&nbsp; Privacy Policy</div>
</div>
</body>
</html>
```